Corwith Lodge website redesign

After 8 years of our current site, we're ready to upgrade our site design. We'd like to generally make it more modern and clean and build it on a CMS like joomla for easier future maintenance.

Our hotel is a family-owned bed and breakfast that competes against much larger hotel chains in Aspen with fancier rooms and larger pricetags. Our hotel is priced moderately and features tasteful, uniquely-design rooms.

We are looking for a website that will showcase the uniqueness of our rooms, the history of the Lodge, and the friendliness of our staff.

Here are some other hotel sites we like:

http://www.brackenfoldhouse.example/

http://www.tollerpeakhaus.example/

http://www.quarrowstay.example/

*********

Scope of Work - I'm looking for a design AND build. The website should be built out in Joomla as part of the final deliverable.
Updates

Current website: http://www.corwithlodge.example/

Explanation of what design + build means:

I am looking for not only the design of the site, but also for the homepage and one subpage to be built out as well. I do NOT need the entire site built - only for those two pages to be built and I will retrofit the remainder of the pages.

Target Market(s)

travellers evaluating hotels in Aspen, Colorado.

Industry/Entity Type

Hotel

Requirements
Must have
• Must, must, must be based on a joomla template. "Rotating" large main image as central position on homepage is a must (see example websites mentioned above).

Nice to have
• We have an existing online reservation system. It would be nice to evaluate placing a "widget" on the homepage that integrates to the online reservation page. Similar to that feature that the Bracken Fold website has at the foot of the main image on their homepage.

```html
<!DOCTYPE html>
<html lang="en">
<head>
<meta charset="utf-8">
<title>Corwith Lodge</title>
<link href="https://fonts.googleapis.com/css2?family=Dosis:wght@300;400;500&display=swap" rel="stylesheet">
<style>
:root{
  --ink:#1c1c1c;
  --panel:#161616;
  --panel-soft:rgba(12,12,12,.88);
  --red:#e8262f;
  --red-dark:#c81a22;
  --white:#ffffff;
  --grey-text:#8c8c8c;
  --label:#555555;
  --line:#cfcfcf;
  --field-border:#cccccc;
  --navy:#1f2a5a;
  --nav-text:#6b6b6b;
}
*{box-sizing:border-box;margin:0;padding:0}
html,body{width:1200px;height:935px;overflow:hidden;background:var(--white)}
body{position:relative;font-family:Arial,Helvetica,sans-serif;color:var(--grey-text)}
.abs{position:absolute}
.hero{left:0;top:0;width:1200px;height:453px;
  background:linear-gradient(180deg,#3f86d4 0%,#7fb3e6 28%,#a9c0cf 40%,#6c7a5a 55%,#4f7a2e 72%,#3c6a22 100%)}
.hero::after{content:"";position:absolute;inset:0;
  background:linear-gradient(90deg,rgba(60,110,30,.55) 0%,rgba(0,0,0,0) 35%,rgba(0,0,0,0) 65%,rgba(120,100,110,.45) 100%)}
.topbar{left:240px;top:0;width:555px;height:50px;background:var(--white)}
.brand{left:30px;top:11px;font-family:Dosis,sans-serif;font-weight:500;font-size:22px;color:var(--ink)}
.nav{left:211px;top:19px;display:flex;gap:18px;font-size:10px;color:var(--nav-text);list-style:none}
.login-tab{left:795px;top:0;width:82px;height:50px;background:var(--panel);color:var(--white);
  font-family:Dosis,sans-serif;font-size:12px;text-align:center;line-height:50px}
.register-tab{left:877px;top:0;width:83px;height:50px;background:var(--red);color:var(--white);
  font-family:Dosis,sans-serif;font-size:12px;text-align:center;line-height:50px}
.login-panel{left:567px;top:50px;width:310px;height:50px;background:var(--panel)}
.login-field{top:13px;width:118px;height:25px;background:#222;border:1px solid #333;
  font-size:9px;font-style:italic;color:#555;line-height:23px;padding-left:24px}
.login-field svg{position:absolute;left:8px;top:6px}
.login-go{left:269px;top:13px;width:26px;height:25px;background:var(--red);color:var(--white);
  font-family:Dosis,sans-serif;font-weight:500;font-size:14px;text-align:center;line-height:25px}
.res-head{left:240px;top:262px;width:240px;height:48px;background:var(--panel);color:var(--white);
  font-family:Dosis,sans-serif;font-weight:500;font-size:14px;line-height:48px;padding-left:19px}
.res-head svg{position:absolute;right:19px;top:14px}
.res-form{left:240px;top:310px;width:240px;height:280px;background:var(--white)}
.res-label{left:19px;font-size:8px;color:var(--label);letter-spacing:.3px}
.res-input{left:11px;width:218px;height:28px;border:1px solid var(--field-border);border-radius:3px;
  font-size:8px;color:#aaa;line-height:26px;padding-left:10px}
.res-input svg{position:absolute;right:8px;top:5px}
.book-btn{left:145px;top:235px;width:84px;height:28px;border-radius:3px;
  background:linear-gradient(var(--red),var(--red-dark));color:var(--white);
  font-size:11px;font-weight:bold;text-align:center;line-height:28px}
.slide-dots{left:886px;top:280px;display:flex;gap:8px}
.slide-dots span{width:12px;height:12px;border:2px solid #111;background:rgba(255,255,255,.25)}
.caption{left:480px;top:310px;width:480px;height:106px;background:var(--panel-soft);color:var(--white);padding:12px 16px}
.caption h1{font-family:Dosis,sans-serif;font-weight:300;font-size:35px;line-height:40px}
.caption p{font-family:Dosis,sans-serif;font-weight:300;font-size:13px;line-height:14px;margin-top:10px;color:#ddd}
.news{top:444px;width:229px}
.news h2{font-family:Dosis,sans-serif;font-weight:400;font-size:14px;color:#444;padding-bottom:9px;border-bottom:1px solid var(--line)}
.news p{font-size:9px;line-height:13.5px;margin-top:12px;width:214px}
.news a{display:block;margin-top:14px;font-size:8.5px;color:#333;text-decoration:none}
.feature{top:600px;width:228px}
.feature-photo{height:87px}
.feature h3{font-size:9.5px;font-weight:bold;color:var(--navy);margin-top:17px}
.feature p{font-size:9px;line-height:13.5px;margin-top:1px}
.footer-rule{top:818px;height:1px;background:var(--line)}
.footer-mark{left:591px;top:811px;width:18px;height:14px;border-radius:50%;background:#777}
.copyright{left:240px;top:842px;font-size:9px}
.social{top:858px;width:15px;height:15px;border-radius:2px}
.legal{right:240px;top:843px;font-size:8px;color:#555}
</style>
</head>
<body>
<div class="abs hero" role="img" aria-label="Photograph of a green Aspen mountain valley with wildflowers under a blue sky with clouds"></div>

<header class="abs topbar">
  <div class="abs brand">Corwith Lodge</div>
  <ul class="abs nav">
    <li>About us</li><li>Rooms</li><li>Reservations</li><li>About Aspen</li><li>Contact us</li>
  </ul>
</header>
<div class="abs login-tab">LOGIN</div>
<div class="abs register-tab">REGISTER</div>

<div class="abs login-panel">
  <div class="abs login-field" style="left:16px">
    <svg width="9" height="10" viewBox="0 0 9 10"><circle cx="4.5" cy="3" r="2.5" fill="#555"/><path d="M0 10 Q4.5 4 9 10Z" fill="#555"/></svg>login</div>
  <div class="abs login-field" style="left:143px">
    <svg width="9" height="11" viewBox="0 0 9 11"><rect x="0" y="5" width="9" height="6" fill="#555"/><path d="M2 5V3a2.5 2.5 0 0 1 5 0v2" stroke="#555" stroke-width="1.5" fill="none"/></svg>password</div>
  <div class="abs login-go">&gt;</div>
</div>

<div class="abs res-head">Online Reservation
  <svg width="16" height="19" viewBox="0 0 16 19"><rect x="0" y="2" width="16" height="17" fill="#fff"/><rect x="3" y="0" width="2" height="4" fill="#fff"/><rect x="11" y="0" width="2" height="4" fill="#fff"/>
  <g fill="#161616"><rect x="2" y="7" width="3" height="2.5"/><rect x="6.5" y="7" width="3" height="2.5"/><rect x="11" y="7" width="3" height="2.5"/><rect x="2" y="11" width="3" height="2.5"/><rect x="6.5" y="11" width="3" height="2.5"/><rect x="11" y="11" width="3" height="2.5"/><rect x="2" y="15" width="3" height="2.5"/><rect x="6.5" y="15" width="3" height="2.5"/></g></svg>
</div>

<form class="abs res-form">
  <div class="abs res-label" style="top:23px">ARRIVAL</div>
  <div class="abs res-input" style="top:36px">Arrival Date
    <svg width="16" height="16" viewBox="0 0 16 16"><rect x="1" y="2" width="14" height="13" fill="none" stroke="#888"/><rect x="1" y="2" width="14" height="3" fill="#888"/><text x="8" y="13" font-size="6" text-anchor="middle" fill="#888" font-family="Arial">23</text></svg></div>
  <div class="abs res-label" style="top:73px">DEPARTURE</div>
  <div class="abs res-input" style="top:85px">Departure Date
    <svg width="16" height="16" viewBox="0 0 16 16"><rect x="1" y="2" width="14" height="13" fill="none" stroke="#888"/><rect x="1" y="2" width="14" height="3" fill="#888"/><text x="8" y="13" font-size="6" text-anchor="middle" fill="#888" font-family="Arial">23</text></svg></div>
  <div class="abs res-label" style="top:123px">ADULTS</div>
  <div class="abs res-input" style="top:134px">0</div>
  <div class="abs res-label" style="top:172px">CHILDREN</div>
  <div class="abs res-input" style="top:185px">0</div>
  <div class="abs book-btn">Book Now</div>
</form>

<div class="abs slide-dots"><span></span><span></span><span></span><span></span></div>

<section class="abs caption">
  <h1>Beatifull Aspen</h1>
  <p>Excepteur sint occaecat cupidatat non proident, sunt in culpa qui officia deserunt mollit anim id est laborum.</p>
</section>

<article class="abs news" style="left:491px">
  <h2>13 August</h2>
  <p>Lorem ipsum dolor sit amet, consectetur adipiscing elit. Aenean ac tortor at tellus feugiat congue quis ut nunc.</p>
  <a href="#">More Info »</a>
</article>
<article class="abs news" style="left:732px">
  <h2>12 August</h2>
  <p>Lorem ipsum dolor sit amet, consectetur adipiscing elit. Aenean ac tortor at tellus feugiat congue quis ut nunc.</p>
  <a href="#">More Info »</a>
</article>

<article class="abs feature" style="left:240px">
  <div class="feature-photo" role="img" aria-label="Photograph of a sea view past a palm tree from a terrace" style="background:linear-gradient(180deg,#4f8fd0 0%,#8bb8e0 45%,#1f4f8a 60%,#2c5a6a 100%)"></div>
  <h3>Phasellus tincidunt viverra enim vitae sodales.</h3>
  <p>Aenean dictum varius felis, mattis sodales eros gravida non. Donec lobortis malesuada nulla, vitae porttitor justo ultrices ac.</p>
</article>
<article class="abs feature" style="left:485px">
  <div class="feature-photo" role="img" aria-label="Photograph of a breakfast plate with melon, beans and a poached egg" style="background:radial-gradient(ellipse at 55% 55%,#f2e7cf 0%,#d9a066 35%,#8a6a3a 70%,#5e5a2e 100%)"></div>
  <h3>Special Offer enim vitae sodales.</h3>
  <p>Aenean dictum varius felis, mattis sodales eros gravida non. Donec lobortis malesuada nulla, vitae porttitor justo ultrices ac.</p>
</article>
<article class="abs feature" style="left:732px">
  <div class="feature-photo" role="img" aria-label="Photograph of a tree silhouetted against an orange sunset sky" style="background:linear-gradient(180deg,#d8431a 0%,#f39a2a 45%,#e96c1c 75%,#3a1a08 100%)"></div>
  <h3>Vix in error iuvaret, at omnium prompta aliquam vel.</h3>
  <p>&nbsp;Sea an porro vide posidonium, eos modus dicit ne. Appetere dignissim vis et. Te per dolore expetenda voluptaria, an eam autem perfecto pratea. Eu eum inermis verterem assentior.</p>
</article>

<footer>
  <div class="abs footer-rule" style="left:240px;width:336px"></div>
  <div class="abs footer-mark" role="img" aria-label="Small decorative footer flourish"></div>
  <div class="abs footer-rule" style="left:624px;width:336px"></div>
  <div class="abs copyright">©&nbsp; 2012&nbsp; All rights reserved.</div>
  <div class="abs social" style="left:240px;background:#3b5a9a"></div>
  <div class="abs social" style="left:258px;background:#5fb6e6"></div>
  <div class="abs legal">Terms of Use Privacy Statement</div>
</footer>
</body>
</html>
```